I need double sided standard sized Business Card [3.5" x 2"]
you choose
Professional
Rik Sorensby
Vice President, Director
Suite 2718 - 845 East Linmore Street
Vancouver, B.C. V5R 3K7
rik@halvenminerals.example
www.halvenminerals.example
would like the logo and maybe a colored background

```html
<!DOCTYPE html>
<html lang="en">
<head>
<meta charset="utf-8">
<title>Halven Minerals Inc – Stationery</title>
<link href="https://fonts.googleapis.com/css2?family=Cinzel:wght@500&family=Open+Sans:wght@400;600&display=swap" rel="stylesheet">
<style>
  :root {
    --backdrop: #8e8f92;
    --paper: #ffffff;
    --brand-blue: #3a5a96;
    --brand-blue-dark: #2f4b80;
    --ink: #4a4f58;
    --ink-soft: #7a7f88;
    --ghost: #e6e8ec;
    --gold-light: #f6c463;
    --gold-dark: #a8701f;
  }
  * { box-sizing: border-box; margin: 0; padding: 0; }
  html, body { width: 1200px; height: 626px; overflow: hidden; }
  body {
    position: relative;
    background: var(--backdrop);
    font-family: "Open Sans", sans-serif;
    color: var(--ink);
  }
  .sheet {
    position: absolute;
    background: var(--paper);
    box-shadow: 0 2px 6px rgba(0,0,0,.35);
    overflow: hidden;
  }
  .wordmark {
    font-family: "Cinzel", serif;
    font-weight: 500;
    color: var(--brand-blue);
    letter-spacing: .04em;
    white-space: nowrap;
  }
  .ghost-mark {
    position: absolute;
    font-family: "Cinzel", serif;
    font-weight: 500;
    color: var(--ghost);
    white-space: nowrap;
  }
  .small-print { font-size: 6px; line-height: 9px; color: var(--ink-soft); }

  /* Business card front */
  .card-front {
    left: 31px; top: 175px; width: 180px; height: 113px;
    background: radial-gradient(circle at 30% 35%, var(--gold-light), var(--gold-dark) 95%);
    border-radius: 6px;
    display: flex; align-items: center; justify-content: center;
  }
  .card-front .wordmark { color: var(--paper); font-size: 15px; }

  /* Business card back */
  .card-back {
    left: 31px; top: 307px; width: 180px; height: 113px;
    border-radius: 6px;
    padding: 16px 14px 0 16px;
  }
  .card-back .name { font-size: 8px; font-weight: 600; color: var(--brand-blue); }
  .card-back .title { font-size: 6px; color: var(--ink-soft); margin-bottom: 8px; }
  .card-back .small-print { font-size: 5.5px; line-height: 8px; }

  /* Letterhead */
  .letterhead { left: 230px; top: 31px; width: 449px; height: 574px; }
  .letterhead .side-band {
    position: absolute; left: 4px; top: 0; width: 14px; height: 100%;
    background: var(--brand-blue);
  }
  .letterhead .head-mark { position: absolute; left: 34px; top: 26px; font-size: 18px; }
  .letterhead .ghost-mark { left: 58px; top: 250px; font-size: 58px; }
  .letterhead .footer {
    position: absolute; left: 34px; bottom: 22px;
    display: flex; gap: 16px;
  }
  .letterhead .footer .col + .col { border-left: 1px solid var(--ghost); padding-left: 16px; }

  /* Envelope back */
  .envelope-back { left: 679px; top: 79px; width: 473px; height: 226px; }

  /* Envelope front */
  .envelope-front { left: 679px; top: 336px; width: 473px; height: 230px; }
  .envelope-front .side-band {
    position: absolute; left: 4px; top: 0; width: 14px; height: 100%;
    background: var(--brand-blue);
  }
  .envelope-front .head-mark { position: absolute; left: 44px; top: 26px; font-size: 16px; }
  .envelope-front .return-address {
    position: absolute; left: 44px; top: 114px;
    display: flex; gap: 16px;
  }
  .envelope-front .ghost-mark { right: 22px; bottom: 26px; font-size: 30px; }
</style>
</head>
<body>

  <section class="sheet card-front" aria-label="Business card front">
    <span class="wordmark">Halven Minerals Inc</span>
  </section>

  <section class="sheet card-back" aria-label="Business card back">
    <p class="name">Rik Sorensby</p>
    <p class="title">Vice President, Director</p>
    <div class="small-print">
      <p>Suite 2718 - 845 East Linmore Street</p>
      <p>Vancouver, B.C. V5R 3K7</p>
      <p>Tel: 604-555-0142</p>
      <p>rik@halvenminerals.example</p>
      <p>www.halvenminerals.example</p>
    </div>
  </section>

  <section class="sheet letterhead" aria-label="Letterhead">
    <div class="side-band"></div>
    <span class="wordmark head-mark">Halven Minerals Inc</span>
    <span class="ghost-mark" aria-hidden="true">Halven</span>
    <div class="footer small-print">
      <div class="col">
        <p>Office: 604-555-0142</p>
        <p>Fax: 604-555-0143</p>
        <p>Cell: 604-555-0144</p>
      </div>
      <div class="col">
        <p>Suite 2718 - 845 East Linmore Street</p>
        <p>Vancouver, B.C. V5R 3K7</p>
        <p>www.halvenminerals.example</p>
      </div>
    </div>
  </section>

  <section class="sheet envelope-back" aria-label="Envelope back">
    <svg width="473" height="226" viewBox="0 0 473 226">
      <path d="M0 0 H473 V40 Q473 118 380 124 H93 Q0 118 0 40 Z" fill="var(--brand-blue)"/>
      <path d="M8 0 V38 Q8 110 95 116 H378 Q465 110 465 38 V0" fill="none" stroke="var(--brand-blue-dark)" stroke-width="1"/>
    </svg>
  </section>

  <section class="sheet envelope-front" aria-label="Envelope front">
    <div class="side-band"></div>
    <span class="wordmark head-mark">Halven Minerals Inc</span>
    <div class="return-address small-print">
      <div>
        <p>Suite 2718 - 845 East Linmore Street</p>
        <p>Vancouver, B.C. V5R 3K7</p>
      </div>
      <div>
        <p>rik@halvenminerals.example</p>
        <p>www.halvenminerals.example</p>
      </div>
    </div>
    <span class="ghost-mark" aria-hidden="true">Halven</span>
  </section>

</body>
</html>
```